BrightNest - Green cleaning service blog design

We have a website, built in wordpress. We need a clean, professional and nice to read blog where we can post articles.

The blog should emphasize images/video and content/text
The blog should be easy to read and see photos
The blog should include navigation to view more articles
The blogs should have categories filters

Your blog design should have a listing page (see a listing of all articles)
Your blog design should have a detail page (full article page)
Your blog design should include responsive mobile and tablet views

You can view our site at
http://brightnest.staging.hostlark.com/

And our blog placeholder page here:
http://brightnest.staging.hostlark.com/blog/

Here are some example blog sites that I like:
https://www.plumhollowgoods.com/healthy-living
https://blog.tuliprow.com/#
http://www.dunmoss.com/blog/

Target Market(s)

mothers, parents, single professionals, enviromentalist

Industry/Entity Type

Cleaning Service

Requirements
Must have
• Reponsive Design (mobile and tablet)
• List page
• Detail page
• Use the header and footer navigation of the existing site:
• http://brightnest.staging.hostlark.com/
• There should be display for "As seen on TV" where we can show what media outlets have covered our story
• - This should live on on the blog landing page (prominently)
• - The should be a widget on the detail page
• Seet the attached image for an example of how this is used on a website (the image is not a blog, but it should give you an idea)

```html
<!DOCTYPE html>
<html lang="en">
<head>
<meta charset="utf-8">
<title>BrightNest Blog</title>
<link href="https://fonts.googleapis.com/css2?family=Open+Sans:wght@400;600;700;800&display=swap" rel="stylesheet">
<style>
:root{
  --black:#141414;
  --ink:#333;
  --muted:#8a8a8a;
  --line:#e3e3e3;
  --blue:#29a9e0;
  --blue-light:#8fd3f2;
  --green:#6cb52d;
  --green-dark:#4f8f1c;
  --white:#fff;
  --panel:#f7f7f7;
}
*{box-sizing:border-box;margin:0;padding:0}
html,body{width:1200px;height:2436px;overflow:hidden}
body{position:relative;background:var(--white);font-family:"Open Sans",Arial,sans-serif;color:var(--ink)}
.abs{position:absolute}

/* header */
.topbar{left:0;top:0;width:1200px;height:76px;background:var(--black)}
.brand{left:248px;top:22px;display:flex;align-items:center;gap:10px;color:var(--white);font-weight:700;font-size:22px}
.brand-dot{width:22px;height:22px;border-radius:50%;background:var(--green)}
.top-phone{left:482px;top:28px;color:var(--white);font-size:15px;font-weight:600;display:flex;align-items:center;gap:8px}
.btn-schedule{left:760px;top:22px;width:96px;height:32px;background:var(--green);color:var(--white);font-size:12px;font-weight:700;border-radius:3px;display:flex;align-items:center;justify-content:center}
.badge{left:872px;top:16px;width:58px;height:44px;background:#eaf5df;border-radius:6px}
.navbar{left:0;top:76px;width:1200px;height:22px;background:var(--blue)}
.nav{right:252px;top:0;height:22px;display:flex;gap:26px;align-items:center;color:var(--white);font-size:11px;font-weight:600}

/* hero */
.hero{left:0;top:98px;width:1200px;height:420px;background:linear-gradient(100deg,#6d6a66 0%,#a29a90 35%,#cbbfb1 60%,#5a3d2c 85%,#3b2a20 100%)}
.hero-box{left:248px;top:220px;width:312px;height:178px;background:rgba(108,181,45,.88);color:var(--white);padding:18px 20px}
.hero-box h2{font-size:15px;font-weight:800;line-height:1.3;text-transform:uppercase}
.hero-box p{font-size:13px;line-height:1.45;margin-top:8px;opacity:.95}
.hero-box .hero-phone{font-size:16px;font-weight:700;margin-top:12px}
.arrow{top:284px;width:34px;height:34px;border-radius:50%;background:var(--blue);display:flex;align-items:center;justify-content:center}

/* tabs */
.tabs{left:240px;top:596px;width:720px;display:flex;justify-content:space-between}
.tab{display:flex;align-items:baseline;gap:6px;color:var(--ink);font-size:15px;font-weight:700}
.tab b{color:var(--blue);font-size:30px;font-weight:400}
.tab-rule{left:240px;top:650px;width:720px;height:1px;background:var(--line)}

/* cards */
.grid{left:248px;top:720px;width:440px;display:grid;grid-template-columns:212px 212px;column-gap:16px;grid-auto-rows:322px}
.card-media{position:relative;height:168px;background:linear-gradient(135deg,#d9d2c8,#a8a49c)}
.card-media.alt{background:linear-gradient(135deg,#e8e4de,#9a8f83)}
.play{position:absolute;left:86px;top:64px;width:40px;height:40px;border-radius:50%;background:rgba(255,255,255,.9);display:flex;align-items:center;justify-content:center}
.meta{display:flex;gap:14px;margin-top:8px;font-size:10px;color:var(--muted)}
.meta span::before{content:"";display:inline-block;width:7px;height:7px;border:1px solid var(--blue);border-radius:50%;margin-right:4px;vertical-align:-1px}
.card-title{margin-top:6px;font-size:13px;font-weight:800;color:var(--blue);text-transform:uppercase;line-height:1.3}
.card-text{margin-top:4px;font-size:10px;line-height:1.5;color:var(--muted)}
.read-more{display:block;margin-top:3px;font-size:10px;color:var(--blue);font-weight:600}

.pager{left:248px;top:2040px;display:flex;gap:8px;align-items:center;font-size:11px;color:var(--ink)}
.pager .dot{width:22px;height:22px;border-radius:50%;border:1px solid var(--blue);display:flex;align-items:center;justify-content:center;color:var(--blue)}
.pager .dot.on{background:var(--blue);color:var(--white)}

/* sidebar */
.side{left:720px;width:228px}
.widget{border:1px solid var(--line);background:var(--white);padding:10px 12px}
.w-head{font-size:11px;font-weight:700;color:var(--blue);display:flex;align-items:center;gap:6px;padding-bottom:8px;border-bottom:1px solid var(--line)}
.w-head::before{content:"";width:10px;height:10px;background:var(--blue);border-radius:2px}
.field{height:22px;border:1px solid var(--line);margin-top:8px;font-size:9px;color:var(--muted);padding:4px 6px}
.btn-blue{height:22px;margin-top:8px;background:var(--blue);color:var(--white);font-size:10px;font-weight:700;display:flex;align-items:center;justify-content:center}
.social-title{font-size:13px;color:var(--blue);font-weight:600}
.social{display:flex;gap:10px;margin-top:10px}
.social i{width:26px;height:26px;border-radius:50%;border:1px solid var(--blue)}
.cat{display:flex;justify-content:space-between;font-size:10px;color:var(--ink);padding:5px 0;border-bottom:1px solid #f0f0f0}
.cat::after{content:"›";color:var(--blue);font-weight:700}
.recent{display:flex;gap:8px;margin-top:10px}
.recent-img{width:52px;height:40px;background:linear-gradient(135deg,#d5cdc2,#9e968c);flex:none}
.recent p{font-size:9px;line-height:1.4;color:var(--blue)}
.recent small{display:block;font-size:8px;color:var(--muted)}
.contact-line{font-size:10px;color:var(--blue);font-weight:600}

/* footer */
.band{left:0;top:2086px;width:1200px;height:22px;background:var(--blue)}
.footer{left:0;top:2108px;width:1200px;height:328px;background:var(--black);color:var(--white)}
.f-col{top:40px}
.f-brand{font-size:18px;font-weight:700}
.f-line{display:flex;gap:8px;align-items:center;font-size:11px;margin-top:14px}
.f-small{font-size:10px;color:#bbb;line-height:1.6}
.f-head{font-size:15px;font-weight:700}
.f-links{font-size:10px;color:#bbb;line-height:1.8;margin-top:8px}
.btn-green{width:100px;height:28px;background:var(--green);font-size:11px;font-weight:700;display:flex;align-items:center;justify-content:center;margin-top:12px}
.btn-outline{width:110px;height:26px;border:1px solid #777;font-size:10px;display:flex;align-items:center;justify-content:center;margin-top:12px}
</style>
</head>
<body>

<header>
  <div class="abs topbar"></div>
  <div class="abs brand"><span class="brand-dot"></span>BrightNest</div>
  <div class="abs top-phone">
    <svg width="14" height="14" viewBox="0 0 24 24"><path fill="#fff" d="M6.6 10.8a15 15 0 0 0 6.6 6.6l2.2-2.2c.3-.3.7-.4 1-.2 1.1.4 2.3.6 3.6.6.6 0 1 .4 1 1V20c0 .6-.4 1-1 1A17 17 0 0 1 3 4c0-.6.4-1 1-1h3.5c.6 0 1 .4 1 1 0 1.3.2 2.5.6 3.6.1.3 0 .7-.2 1z"/></svg>
    1.800.555.0142
  </div>
  <div class="abs btn-schedule">Schedule Now</div>
  <div class="abs badge"></div>
  <div class="abs navbar">
    <nav class="abs nav"><span>Home</span><span>Services</span><span>About</span><span>Categories</span><span>Contact</span></nav>
  </div>
</header>

<section>
  <div class="abs hero" role="img" aria-label="Smiling cleaning professional in a bright home"></div>
  <div class="abs hero-box">
    <h2>A safer, cleaner home at one affordable price. Sign up</h2>
    <p>You don't just get a cleaner home, you get a healthier one. We use green, plant-based products.</p>
    <div class="hero-phone">Phone: 1.800.555.0142</div>
  </div>
  <div class="abs arrow" style="left:0"><svg width="12" height="12" viewBox="0 0 12 12"><path d="M8 1 3 6l5 5" stroke="#fff" stroke-width="2" fill="none"/></svg></div>
  <div class="abs arrow" style="left:1166px"><svg width="12" height="12" viewBox="0 0 12 12"><path d="m4 1 5 5-5 5" stroke="#fff" stroke-width="2" fill="none"/></svg></div>
</section>

<div class="abs tabs">
  <div class="tab"><b>01</b>BLOG ARTICLE</div>
  <div class="tab"><b>02</b>BLOG ARTICLE</div>
  <div class="tab"><b>03</b>BLOG ARTICLE</div>
  <div class="tab"><b>04</b>BLOG ARTICLE</div>
</div>
<div class="abs tab-rule"></div>

<main class="abs grid">
  <article>
    <div class="card-media" role="img" aria-label="Cleaner tidying an apartment living room"></div>
    <div class="meta"><span>MAY 18, 2017</span><span>12 Comments</span></div>
    <h3 class="card-title">Apartments, Houses &amp; Lofts</h3>
    <p class="card-text">We use plant-based products in every room so your family breathes easy. Our team works fast, treats your space with care and leaves no harsh smell behind.</p>
    <span class="read-more">Continue Reading</span>
  </article>
  <article>
    <div class="card-media alt" role="img" aria-label="Cleaner vacuuming a carpet"></div>
    <div class="meta"><span>MAY 18, 2017</span><span>12 Comments</span></div>
    <h3 class="card-title">Carpeting &amp; Upholstery</h3>
    <p class="card-text">Deep cleaning for rugs, sofas and chairs with gentle green solutions that lift stains and dust while keeping fabrics soft and colours bright.</p>
    <span class="read-more">Continue Reading</span>
  </article>
  <article>
    <div class="card-media alt" role="img" aria-label="Cleaner wiping a window"></div>
    <div class="meta"><span>MAY 18, 2017</span><span>12 Comments</span></div>
    <h3 class="card-title">Windows</h3>
    <p class="card-text">Streak-free glass inside and out, using simple natural cleaners that are safe for kids and pets and kind to the planet we all share.</p>
    <span class="read-more">Continue Reading</span>
  </article>
  <article>
    <div class="card-media" role="img" aria-label="Cleaning professional holding supplies"></div>
    <div class="meta"><span>MAY 18, 2017</span><span>12 Comments</span></div>
    <h3 class="card-title">Home Cleaning</h3>
    <p class="card-text">Regular visits that keep every room fresh, from kitchen counters to bathroom tiles, planned around your week and your own checklist.</p>
    <span class="read-more">Continue Reading</span>
  </article>
  <article>
    <div class="card-media" role="img" aria-label="Video still of a cleaner at work">
      <span class="play"><svg width="14" height="14" viewBox="0 0 14 14"><path d="M3 1v12l10-6z" fill="#29a9e0"/></svg></span>
    </div>
    <div class="meta"><span>MAY 18, 2017</span><span>12 Comments</span></div>
    <h3 class="card-title">10 Things You Should Be Cleaning Each Week</h3>
    <p class="card-text">Small spots hide a lot of dust and germs. Here is a simple list to keep your home healthy with only a few minutes a day.</p>
    <span class="read-more">Continue Reading</span>
  </article>
  <article>
    <div class="card-media alt" role="img" aria-label="Video still of a bright rental bedroom">
      <span class="play"><svg width="14" height="14" viewBox="0 0 14 14"><path d="M3 1v12l10-6z" fill="#29a9e0"/></svg></span>
    </div>
    <div class="meta"><span>MAY 18, 2017</span><span>12 Comments</span></div>
    <h3 class="card-title">Vacation Rental Cleaning</h3>
    <p class="card-text">Fast turnovers between guests with fresh linens, spotless baths and a calm, clean welcome that earns great reviews every stay.</p>
    <span class="read-more">Continue Reading</span>
  </article>
  <article>
    <div class="card-media alt" role="img" aria-label="Video still of electronics being dusted">
      <span class="play"><svg width="14" height="14" viewBox="0 0 14 14"><path d="M3 1v12l10-6z" fill="#29a9e0"/></svg></span>
    </div>
    <div class="meta"><span>MAY 18, 2017</span><span>12 Comments</span></div>
    <h3 class="card-title">Other Electrical Device</h3>
    <p class="card-text">Safe ways to clean screens, remotes and keyboards without harsh sprays, plus tips on how often each one needs care.</p>
    <span class="read-more">Continue Reading</span>
  </article>
  <article>
    <div class="card-media" role="img" aria-label="Video still of a fresh, airy living room">
      <span class="play"><svg width="14" height="14" viewBox="0 0 14 14"><path d="M3 1v12l10-6z" fill="#29a9e0"/></svg></span>
    </div>
    <div class="meta"><span>MAY 18, 2017</span><span>12 Comments</span></div>
    <h3 class="card-title">How to Improve the Air Quality in Your Home</h3>
    <p class="card-text">Plants, fresh air and green products all help. Learn easy habits that make every breath at home a little cleaner.</p>
    <span class="read-more">Continue Reading</span>
  </article>
</main>

<nav class="abs pager">
  <span class="dot">‹</span><span class="dot on">1</span><span>2</span><span>3</span><span>4</span><span class="dot">›</span>
</nav>

<aside>
  <div class="abs side widget" style="top:728px">
    <div class="w-head">Search</div>
    <div class="field">Keywords</div>
    <div class="btn-blue">Search</div>
  </div>

  <div class="abs side" style="top:882px">
    <div class="social-title">Social Channels</div>
    <div class="social"><i></i><i></i><i></i><i></i></div>
  </div>

  <div class="abs side widget" style="top:1010px">
    <div class="w-head">Categories</div>
    <div class="cat">Carpets</div>
    <div class="cat">Cleaning</div>
    <div class="cat">Eco Tips</div>
    <div class="cat">Office Cleaning</div>
    <div class="cat">Healthy Home</div>
    <div class="cat">Natural Products</div>
    <div class="cat">Vacation Rentals</div>
  </div>

  <div class="abs side widget" style="top:1240px">
    <div class="w-head">Sign Up</div>
    <div class="field">Name</div>
    <div class="field">Email</div>
    <div class="btn-blue">Subscribe</div>
  </div>

  <div class="abs side widget" style="top:1420px">
    <div class="w-head">Recent Articles</div>
    <div class="recent"><div class="recent-img" role="img" aria-label="Kitchen thumbnail"></div><p>Green kitchen habits for busy parents<small>May 18, 2017</small></p></div>
    <div class="recent"><div class="recent-img" role="img" aria-label="Office thumbnail"></div><p>Office cleaning done the natural way<small>May 18, 2017</small></p></div>
    <div class="recent"><div class="recent-img" role="img" aria-label="Carpet thumbnail"></div><p>Caring for carpets without harsh sprays<small>May 18, 2017</small></p></div>
  </div>

  <div class="abs side widget" style="top:1684px">
    <div class="w-head">As Seen On TV</div>
    <div class="btn-blue">View Media</div>
  </div>

  <div class="abs side contact-line" style="top:1800px">CONTACT US: 1.800.555.0142</div>
</aside>

<div class="abs band"></div>
<footer class="abs footer">
  <div class="abs f-col" style="left:248px">
    <div class="f-brand">BrightNest</div>
    <div class="f-line"><svg width="12" height="12" viewBox="0 0 24 24"><path fill="#fff" d="M6.6 10.8a15 15 0 0 0 6.6 6.6l2.2-2.2c.3-.3.7-.4 1-.2 1.1.4 2.3.6 3.6.6.6 0 1 .4 1 1V20c0 .6-.4 1-1 1A17 17 0 0 1 3 4c0-.6.4-1 1-1h3.5c.6 0 1 .4 1 1 0 1.3.2 2.5.6 3.6.1.3 0 .7-.2 1z"/></svg>1.800.555.0142</div>
    <div class="f-small" style="margin:6px 0 0 20px">Mon to Fri, 8am – 6pm<br>Sat by appointment</div>
    <div class="f-line"><svg width="12" height="14" viewBox="0 0 24 28"><path fill="#fff" d="M12 0a10 10 0 0 0-10 10c0 7 10 18 10 18s10-11 10-18A10 10 0 0 0 12 0zm0 14a4 4 0 1 1 0-8 4 4 0 0 1 0 8z"/></svg>14 Alder Row, Suite 210</div>
    <div class="f-small" style="margin:4px 0 0 20px">Brookfield, NY 10012</div>
  </div>
  <div class="abs f-col" style="left:520px">
    <div class="f-head">company</div>
    <div class="f-links">About<br>Careers<br>Contact</div>
    <div class="f-head" style="margin-top:16px">what we do</div>
    <div class="f-links">Services<br>Pricing<br>Blog</div>
  </div>
  <div class="abs f-col" style="left:752px">
    <div class="f-head">book online now!</div>
    <div class="btn-green">Schedule Now</div>
    <div class="f-small" style="margin-top:10px;width:200px">Get a green home without the hassle.<br>Sign up today for special offers and news.</div>
    <div class="btn-outline">join our mailing list</div>
  </div>
</footer>

</body>
</html>
```